Church needs a graphic design/flyer layout for upcoming series

I need a multi-purpose design for promoting both our upcoming series of messages and our fall kick-off event where we will launch the messages.

Our promotion will be printed on a two-sided. One side is simple and focuses on the series and the other side has details in regards to the event. I have provided an attachment example of what we did last time.

The design needs to be multi-purpose because it will be used for our sermon Power Points, placed on our website banner, social media, etc.

• Sermon series is called “Quiet Questions”
• The subtitle will be “What’s keeping you from God?”
• Our name logo should be on the graphic as well.
• The subject manner will revolve around common hurdles that people face about God and Christianity: The existence of God, the exclusivity of religion, Hell, the reliability of the Bible, Hypocrisy in the church, etc.
• Our mission is “Connecting Young Families to Christ” so our focus is to reach out to families while not being exclusive to others.
• Our target audience is families with school-aged kids.
• This series is an invitational focus so we want it to be appealing to non-church goers.
• It should be attention grabbing while not being too ‘edgy’

• The front of the card will most likely consist the Sermon Series Graphic, title & subtitle of the series, and perhaps our name logo somewhere on it.
• The back of the card will invite and give the basic information for the event so that the people will be encouraged to save the date and come to the event.
• Here are some things that could be included on that advertisement:
o The name of the event: “Harbor Church Fall Kick-off”
o The date and time of the event: Sept 23rd @ 10:30
o Features of the event:
 Free lunch
 Children’s program
 Bouncy Castle
 Start of the “Quiet Questions” messages.
 Sample of topics
o Information about the church: our website and address, etc
o Engaging pictures and graphics.
• The rest of the tone and manner are the same as the sermon series graphic.
The flyer will be 11X14, like a postcard size.

Target Market(s)

Young families who are spiritually curious but not committed church attenders.

Colors

Designer to choose colors to be used in the design.

Requirements
Nice to have
• A modern and professional looking design.
Should not have
• Anything offensive or not family friendly.

```html
<!DOCTYPE html>
<html lang="en">
<head>
<meta charset="utf-8">
<title>Quiet Questions – Harbor Church Fall Kick-off</title>
<link rel="stylesheet" href="https://fonts.googleapis.com/css2?family=Crimson+Text:wght@400;600;700&display=swap">
<style>
  :root {
    --purple: #8a2a8c;
    --purple-deep: #7b2280;
    --orange: #f6901e;
    --blue: #2f7fc1;
    --blue-deep: #1f6db4;
    --paper: #ffffff;
    --note: #ececec;
    --ink: #1f1f1f;
  }
  * { box-sizing: border-box; margin: 0; padding: 0; }
  html, body { width: 1200px; height: 1200px; overflow: hidden; background: var(--paper); }
  body { position: relative; font-family: "Crimson Text", Georgia, serif; }

  .card {
    position: absolute; left: 264px; width: 638px; height: 502px;
    overflow: hidden; box-shadow: 2px 2px 4px rgba(0,0,0,.35);
  }
  .card--front { top: 76px; }
  .card--back { top: 630px; }

  .scene { position: absolute; inset: 0; }
  .scene--meadow {
    background:
      radial-gradient(ellipse at 78% 30%, #fffaf2 0%, rgba(255,250,242,0) 45%),
      linear-gradient(180deg, #fdfbf8 0%, #f6efe7 38%, #d8c7b4 62%, #b59a5e 78%, #8f8c3c 100%);
  }
  .scene--field {
    background: linear-gradient(180deg, #fbf8f5 0%, #e9e2da 22%, #4a5a3a 36%, #7a6a5a 60%, #6e8fb0 100%);
  }

  .brand {
    position: absolute; left: 96px; top: 44px; width: 250px; text-align: center;
  }
  .brand__mark {
    width: 76px; height: 76px; margin: 0 auto 14px; border-radius: 50%; background: var(--purple);
  }
  .brand__name { font-size: 21px; font-weight: 400; color: var(--ink); white-space: nowrap; }

  .band { position: absolute; left: 0; }
  .band--title { top: 185px; width: 400px; height: 115px; }
  .band--subtitle { top: 319px; width: 392px; height: 115px; }
  .band svg { position: absolute; inset: 0; }

  .series-title {
    position: absolute; left: 0; width: 392px; top: 216px; text-align: center;
    font-size: 50px; font-weight: 700; color: var(--purple); line-height: 1;
  }
  .series-subtitle {
    position: absolute; left: 0; width: 392px; top: 330px; text-align: center;
    font-size: 38px; font-weight: 600; color: #fff; line-height: 1.2;
  }

  .overlay-purple {
    position: absolute; left: 0; top: 190px; width: 638px; height: 210px;
    background: linear-gradient(90deg, rgba(123,34,128,.96) 0%, rgba(138,42,140,.9) 100%);
  }
  .overlay-blue {
    position: absolute; left: 0; top: 399px; width: 638px; height: 103px;
    background: rgba(47,127,193,.92);
  }
  .top-white {
    position: absolute; left: 260px; top: 0; width: 378px; height: 126px; background: var(--paper);
  }

  .calendar {
    position: absolute; left: 52px; top: 42px; width: 188px; height: 222px;
    background: var(--note); transform: rotate(3deg); box-shadow: 1px 2px 4px rgba(0,0,0,.25);
  }
  .calendar__month {
    height: 44px; background: var(--blue-deep); color: #fff; text-align: center;
    font-size: 21px; font-weight: 600; letter-spacing: .5px; line-height: 50px;
  }
  .calendar__day {
    text-align: center; font-size: 96px; font-weight: 700; color: var(--blue-deep); line-height: 1; margin-top: 4px;
  }
  .calendar__rule { height: 2px; background: var(--blue-deep); margin: 14px 12px 0; }
  .calendar__time {
    padding-left: 14px; font-size: 40px; font-weight: 700; color: var(--blue-deep); line-height: 1.3;
  }
  .pin { position: absolute; left: 164px; top: 24px; }

  .event-title {
    position: absolute; right: 48px; top: 22px; text-align: right;
    font-size: 42px; font-weight: 700; color: var(--purple); line-height: 1.2;
  }
  .features-band {
    position: absolute; left: 268px; top: 126px; width: 370px; height: 65px; background: var(--orange);
    color: #fff; font-size: 33px; font-weight: 600; line-height: 65px; padding-left: 16px;
  }
  .features {
    position: absolute; right: 48px; top: 212px; list-style: none; text-align: right;
    color: #fff; font-size: 29px; font-weight: 600; line-height: 35px;
  }

  .contact {
    position: absolute; left: 44px; width: 548px; top: 418px;
    display: flex; justify-content: space-between; color: #fff; font-size: 15px; font-weight: 600;
  }
  .contact__item { display: flex; align-items: center; gap: 8px; }
  .contact__rule { position: absolute; left: 44px; top: 453px; width: 548px; height: 1px; background: #fff; }
  .address {
    position: absolute; left: 0; width: 638px; top: 466px; text-align: center;
    color: #fff; font-size: 15px; font-weight: 600;
  }
</style>
</head>
<body>

<section class="card card--front">
  <div class="scene scene--meadow" role="img" aria-label="Sunlit meadow photograph with a woman raising her arms in worship"></div>

  <div class="brand">
    <div class="brand__mark"></div>
    <div class="brand__name">Westbrook Harbor Church</div>
  </div>

  <div class="band band--title">
    <svg width="400" height="115" viewBox="0 0 400 115"><polygon points="0,0 392,0 400,115 0,115" fill="var(--orange)"/></svg>
  </div>
  <h1 class="series-title">Quiet Questions</h1>

  <div class="band band--subtitle">
    <svg width="392" height="115" viewBox="0 0 392 115"><polygon points="0,0 390,0 380,115 0,115" fill="var(--purple)"/></svg>
  </div>
  <p class="series-subtitle">What’s keeping<br>you from God?</p>
</section>

<section class="card card--back">
  <div class="scene scene--field" role="img" aria-label="Soft-focus field and tree line photograph"></div>
  <div class="top-white"></div>
  <div class="overlay-purple"></div>
  <div class="overlay-blue"></div>

  <div class="calendar">
    <div class="calendar__month">SEPTEMBER</div>
    <div class="calendar__day">23</div>
    <div class="calendar__rule"></div>
    <div class="calendar__time">at 10:30</div>
  </div>
  <svg class="pin" width="24" height="28" viewBox="0 0 24 28">
    <rect x="10" y="12" width="4" height="14" fill="#1b4f86"/>
    <circle cx="12" cy="11" r="10" fill="#245f9e"/>
  </svg>

  <h2 class="event-title">Harbor Church<br>Fall Kick-off</h2>

  <div class="features-band">Features of the event</div>
  <ul class="features">
    <li>Free lunch</li>
    <li>Children’s program</li>
    <li>Bouncy Castle</li>
    <li>Start of the “Quiet Questions” messages</li>
    <li>Sample of topics</li>
  </ul>

  <div class="contact">
    <span class="contact__item">
      <svg width="18" height="18" viewBox="0 0 24 24"><path d="M6.6 10.8a15 15 0 0 0 6.6 6.6l2.2-2.2c.3-.3.7-.4 1-.2 1.1.4 2.3.6 3.6.6.6 0 1 .4 1 1V20c0 .6-.4 1-1 1A17 17 0 0 1 3 4c0-.6.4-1 1-1h3.5c.6 0 1 .4 1 1 0 1.3.2 2.5.6 3.6.1.3 0 .7-.2 1z" fill="#fff"/></svg>
      555.010.4420
    </span>
    <span class="contact__item">
      <svg width="24" height="16" viewBox="0 0 24 16"><rect x="1" y="1" width="22" height="14" fill="none" stroke="#fff" stroke-width="1.5"/><path d="M1 1l11 8 11-8M1 15l8-7M23 15l-8-7" fill="none" stroke="#fff" stroke-width="1.5"/></svg>
      hello@harborchurch.example
    </span>
    <span class="contact__item">
      <svg width="20" height="20" viewBox="0 0 24 24" fill="none" stroke="#fff" stroke-width="1.4"><circle cx="12" cy="12" r="10"/><ellipse cx="12" cy="12" rx="4.5" ry="10"/><path d="M2 12h20M4 6.5h16M4 17.5h16"/></svg>
      www.harborchurch.example
    </span>
  </div>
  <div class="contact__rule"></div>
  <p class="address">118 Maple Crescent, Lakeview, ON K0A 2B0</p>
</section>

</body>
</html>
```